Marlow Crest Homes Needs Business Card Design

Looking for a unique modern business card to fit my new Logo.
Name: Dean Marlow
Company: Marlow Crest Homes, LLC
Tag Line: Forever Framed Right
Email: marlowcresthomes@mailvista.test
Phone: (253) 555-0187
Website: www.marlowcresthomes.test
License: MARLOCH462QT

```html
<!DOCTYPE html>
<html lang="en">
<head>
<meta charset="utf-8">
<title>Marlow Crest Homes — Business Card</title>
<link rel="stylesheet" href="https://fonts.googleapis.com/css2?family=Arimo:wght@400;700&display=swap">
<style>
  :root {
    --bg: #e4e4e4;
    --card-white: #f7f7f8;
    --ink: #1b1b1b;
    --brand-blue: #3a94c6;
    --blue-top: #429bc9;
    --blue-bottom: #318abd;
    --white: #ffffff;
  }
  * { box-sizing: border-box; margin: 0; padding: 0; }
  html, body { width: 1200px; height: 1200px; overflow: hidden; }
  body {
    background: var(--bg);
    font-family: "Arimo", Arial, sans-serif;
    color: var(--ink);
    position: relative;
  }
  .card {
    position: absolute;
    left: 262px;
    width: 686px;
    height: 392px;
    border-radius: 22px;
    overflow: hidden;
  }
  .card--front { top: 165px; background: var(--card-white); }
  .card--back {
    top: 653px;
    background: linear-gradient(180deg, var(--blue-top), var(--blue-bottom));
    color: var(--white);
  }

  .brand {
    position: absolute;
    display: flex;
    align-items: center;
    gap: 12px;
    font-weight: 700;
    letter-spacing: 0.5px;
    white-space: nowrap;
  }
  .brand__square { display: block; background: currentColor; }
  .card--front .brand {
    right: 46px;
    top: 72px;
    font-size: 24px;
    color: var(--ink);
  }
  .card--front .brand__square { width: 26px; height: 26px; background: var(--brand-blue); }

  .holder { position: absolute; left: 49px; top: 212px; }
  .holder__name {
    font-size: 27px;
    font-weight: 700;
    color: var(--brand-blue);
    letter-spacing: 0.3px;
    line-height: 1;
  }
  .holder__role { font-size: 15px; margin-top: 5px; }

  .divider {
    position: absolute;
    left: 49px;
    width: 591px;
    top: 270px;
    height: 1px;
    background: var(--brand-blue);
  }

  .contact { position: absolute; left: 49px; top: 282px; font-size: 15.5px; line-height: 20px; }
  .contact__company { margin-bottom: 6px; }
  .contact__row { display: flex; align-items: center; gap: 7px; }
  .contact__icon { width: 16px; height: 14px; flex: none; }

  .web { position: absolute; right: 46px; top: 308px; text-align: right; font-size: 15.5px; line-height: 20px; }

  .card--back .brand {
    left: 0; right: 0; top: 150px;
    justify-content: center;
    font-size: 38px;
    color: var(--white);
  }
  .card--back .brand__square { width: 36px; height: 36px; }
  .tagline {
    position: absolute;
    left: 0; right: 0; top: 327px;
    text-align: center;
    font-size: 18px;
  }
</style>
</head>
<body>
  <section class="card card--front" aria-label="Card front">
    <div class="brand"><span class="brand__square"></span>MARLOW CREST HOMES</div>

    <div class="holder">
      <h1 class="holder__name">DEAN MARLOW</h1>
      <p class="holder__role">Residential Builder</p>
    </div>

    <div class="divider"></div>

    <div class="contact">
      <p class="contact__company">Marlow Crest Homes, LLC</p>
      <p class="contact__row">
        <svg class="contact__icon" viewBox="0 0 24 24" aria-hidden="true"><path fill="#1b1b1b" d="M6.6 10.8a15.1 15.1 0 0 0 6.6 6.6l2.2-2.2c.3-.3.7-.4 1-.2 1.1.4 2.3.6 3.6.6.6 0 1 .4 1 1V20c0 .6-.4 1-1 1A17 17 0 0 1 3 4c0-.6.4-1 1-1h3.5c.6 0 1 .4 1 1 0 1.3.2 2.5.6 3.6.1.3 0 .7-.2 1l-2.3 2.2z"/></svg>
        (253) 555-0187
      </p>
      <p class="contact__row">
        <svg class="contact__icon" viewBox="0 0 24 18" aria-hidden="true"><rect x="1" y="2" width="22" height="14" fill="#1b1b1b"/><path d="M2 3l10 7 10-7" fill="none" stroke="#f7f7f8" stroke-width="1.8"/></svg>
        marlowcresthomes@mailvista.test
      </p>
    </div>

    <div class="web">
      <p>www.marlowcresthomes.test</p>
      <p>Lic : MARLOCH462QT</p>
    </div>
  </section>

  <section class="card card--back" aria-label="Card back">
    <div class="brand"><span class="brand__square"></span>MARLOW CREST HOMES</div>
    <p class="tagline">Forever Framed Right</p>
  </section>
</body>
</html>
```